依頼詳細
RPE歯科クリニック~行きます訪問歯科・送迎歯科~
のパンフレットを作成依頼致します。

1.パンフレットに使用したいデータ等がございません。以前使用していたパンフレットをPDFで添付いたしますのでご確認ください。添付エクセルデータがございます。こちらを参考にA4両面に収めてレイアウトしてください。

2. パンフレットは以前のパンフレットの(ピンク×水色、ピンク、水色)を希望しております。

3.1枚目の車のロゴはないので、作成いただいてもフリー素材でも結構ですのでお願い致します。

4.MAPは、添付フィル≪MAP_image≫をご確認ください。

5.仕上がりはA4両面イラストレーターデザインを希望いたします。フルカラーでお願いします。
サイズ
A4
ページ数
4ページ
希望イメージ
シンプル 複雑
単色 カラフル
暗い 明るい
日常 高級
遊び心 厳粛
未来的 伝統的
女性的 男性的
希望する色
赤系、水色系
納品ファイル
• イラストレーター形式 (.ai)
補足説明
修正致します

1.添付エクセルデータがございます。→PDFデータの為、文字おこしお願い致します。
医院名
RPE歯科クリニック
~行きます訪問歯科・送迎歯科~
パンフレットのカテゴリになっておりますが、
A4サイズ両面のチラシ作成依頼になります。

よろしくお願いいたします。
コンペ当選者を確約に変更いたしましたのでよろしくお願いいたします。

色使いや、歯を使ったイラストの可愛さと、全体的に見やすくバランスが良かったです。

たくさんのご提案ありがとうございました。 慣れない依頼にご提案くださり感謝しています。 また、機会がありましたら是非ご協力ください。 ありがとうございました。

```html
<!DOCTYPE html>
<html lang="ja">
<head>
<meta charset="utf-8">
<title>RPE歯科医院 訪問診療のご案内</title>
<link rel="stylesheet" href="https://fonts.googleapis.com/css2?family=M+PLUS+Rounded+1c:wght@400;700;800&display=swap">
<style>
:root{
  --mint:#9fdccf;
  --mint-deep:#5fbfae;
  --mint-pale:#d6f1ea;
  --pink:#e8628c;
  --pink-deep:#d94778;
  --pink-soft:#f6bfd1;
  --pink-pale:#fbe3eb;
  --white:#ffffff;
  --ink:#4a4a4a;
}
*{margin:0;padding:0;box-sizing:border-box}
html,body{width:849px;height:1200px;overflow:hidden;background:var(--white)}
body{font-family:"M PLUS Rounded 1c",sans-serif;color:var(--ink)}
.sheet{position:relative;width:849px;height:1200px;overflow:hidden;
  background:linear-gradient(160deg,var(--pink-pale) 0%,var(--pink-soft) 60%,#f3a9c1 100%)}
.header{position:absolute;left:0;top:0;width:849px;height:320px;
  background:linear-gradient(180deg,var(--mint-deep) 0%,var(--mint) 70%,var(--mint-pale) 100%)}
.tagline{position:absolute;left:40px;top:30px;font-size:36px;font-weight:800;color:var(--white);letter-spacing:2px;white-space:nowrap}
.clinic-name{position:absolute;left:40px;top:88px;font-size:58px;font-weight:800;color:var(--white);letter-spacing:3px;white-space:nowrap;line-height:1.2}
.scene{position:absolute;left:430px;top:168px;width:390px;height:152px;border-radius:12px 12px 0 0;
  background:linear-gradient(180deg,#cbeee6,#f4faf8)}
.intro{position:absolute;left:57px;top:335px;width:735px;height:130px;background:var(--pink);
  color:var(--white);text-align:center;padding-top:22px;font-size:20px;line-height:1.65;font-weight:700}
.intro .lead{font-size:21px}
.pill{position:absolute;height:44px;border-radius:22px;background:var(--pink);color:var(--white);
  font-size:22px;font-weight:800;display:flex;align-items:center;justify-content:center;letter-spacing:4px}
.pill.treat{left:57px;top:498px;width:275px}
.pill.flow{left:368px;top:498px;width:438px}
.treat-card{position:absolute;left:57px;width:275px;background:var(--mint);border-radius:14px;
  display:flex;align-items:center;padding:0 12px;gap:8px}
.treat-card p{flex:1;font-size:15px;font-weight:700;line-height:1.6;color:var(--ink);white-space:nowrap}
.treat-card .art{flex:none;width:84px;height:76px;border-radius:38px;background:linear-gradient(135deg,#ffffff,#cfeee7)}
.c1{top:565px;height:150px}.c2{top:735px;height:140px}.c3{top:895px;height:140px}.c4{top:1055px;height:110px}
.step{position:absolute;left:368px;width:438px}
.step .num{position:absolute;left:0;top:0;width:46px;height:46px;border-radius:50%;background:var(--pink);
  color:var(--white);font-size:24px;font-weight:800;display:flex;align-items:center;justify-content:center;border:3px solid var(--white)}
.step h3{margin-left:30px;height:40px;background:var(--pink);color:var(--white);font-size:19px;font-weight:800;
  padding-left:30px;display:flex;align-items:center;border-radius:0 20px 20px 0;margin-top:3px}
.step .desc{background:var(--white);margin-left:30px;padding:10px 14px;font-size:14px;line-height:1.6;font-weight:400}
.s1{top:565px}.s2{top:680px}.s3{top:795px}.s4{top:910px}.s5{top:1045px}
</style>
</head>
<body>
<main class="sheet">
  <header class="header">
    <div class="tagline">行きます訪問・送迎歯科クリニック</div>
    <h1 class="clinic-name">RPE 歯科医院</h1>
    <div class="scene" role="img" aria-label="クリニックの家と送迎車のイラスト"></div>
  </header>

  <section class="intro">
    <p class="lead">訪問診療とは</p>
    <p>介護施設や自宅で寝たきりの方や歩行が困難で通院できない方<br>のもとへ歯科医師や歯科衛生士が訪問を行う医療サービスです。</p>
  </section>

  <div class="pill treat">治　療</div>
  <div class="treat-card c1"><p>虫歯、歯周病の治療、<br>予防</p><div class="art" role="img" aria-label="歯と歯ブラシのイラスト"></div></div>
  <div class="treat-card c2"><p>入れ歯の作製<br>修理、調整</p><div class="art" role="img" aria-label="入れ歯のイラスト"></div></div>
  <div class="treat-card c3"><p>口腔ケアで<br>感染症予防</p><div class="art" role="img" aria-label="歯のキャラクターのイラスト"></div></div>
  <div class="treat-card c4"><p>お口のリハビリ</p></div>

  <div class="pill flow">訪問診療の流れ</div>

  <div class="step s1"><div class="num">1</div><h3>お申込み</h3><p class="desc">お電話・FAXなどでお気軽にお申込みください。</p></div>
  <div class="step s2"><div class="num">2</div><h3>訪問日の調整</h3><p class="desc">ご希望に合わせて訪問日を設定します。</p></div>
  <div class="step s3"><div class="num">3</div><h3>無料検診</h3><p class="desc">お口の状態を診察します。費用は一切かかりません。</p></div>
  <div class="step s4"><div class="num">4</div><h3>治　療</h3><p class="desc">訪問診療を開始します。初診時・月始めは、各種保険証が必要になります。一回の診療時間は３０分程度です。</p></div>
  <div class="step s5"><div class="num">5</div><h3>今後のご相談</h3><p class="desc">定期健診やフラッシング等のアフターケアのため定期的に訪問します。定期健診の結果により治療を再開します。</p></div>
</main>
</body>
</html>
```